Text design/overlay needed for promotional music release cover photo

I need the following text elements added to the attached image:
Element 1: Brent Colfax and The Kinship Circle
Element 2. This all needs to be clear and prominent : Featuring: Warren Petty, Corey Halvin, Renata Bloor, Ingrid Palumbo, Martin "Chipper" Lowe, Tamara Ridgely, Wa Ni Po Glen Harker, Nolan Brackett, Otis Crane, Dustin Pell, and The Final Grooveling
Element 3 ("WILLOW BEND" needs to pop): New single WILLOW BEND available everywhere 9/26
The final image needs to be 16:9 ratio. Colors should be black and samples from the bench in the image. Various fonts, text sizes, etc. The music is a reggae/bluegrass blend. I'm looking for art not AI. Thanks!

```html
<!DOCTYPE html>
<html lang="en">
<head>
<meta charset="utf-8">
<title>Brent Colfax and The Kinship Circle – Willow Bend</title>
<link rel="stylesheet" href="https://fonts.googleapis.com/css2?family=Anton&family=Archivo:wght@800&family=Rubik+Dirt&display=swap">
<style>
  :root {
    --ink: #231f20;
    --outline: #f5e04a;
    --cream: #f1ede0;
    --bench-red: #e0261f;
    --bench-yellow: #f7d631;
    --bench-orange: #f07a1c;
    --bench-green: #4c9a2a;
    --bench-lime: #86d67a;
    --bench-blue: #2ea6e8;
    --chip-white: #ffffff;
    --chip-dark: #3b3530;
  }
  * { margin: 0; padding: 0; box-sizing: border-box; }
  html, body { width: 1200px; height: 675px; overflow: hidden; background: #fff; }
  .cover {
    position: relative;
    width: 1200px;
    height: 675px;
    overflow: hidden;
    font-family: "Anton", "Arial Narrow", sans-serif;
  }
  .cover-photo {
    position: absolute; inset: 0;
    background:
      radial-gradient(ellipse 260px 150px at 40px 640px, rgba(247,214,49,.9), rgba(247,214,49,0) 70%),
      radial-gradient(ellipse 170px 110px at 250px 650px, rgba(224,38,31,.85), rgba(224,38,31,0) 70%),
      radial-gradient(ellipse 260px 200px at 1140px 520px, rgba(120,200,90,.85), rgba(120,200,90,0) 70%),
      radial-gradient(ellipse 140px 260px at 560px 560px, rgba(150,140,125,.7), rgba(150,140,125,0) 70%),
      linear-gradient(180deg, #e9efe6 0%, #9fcf5a 30%, #79b83a 55%, #a9a08f 80%, #8f8778 100%);
  }
  .headline {
    position: absolute;
    left: 118px; top: 36px;
    width: 966px; height: 392px;
  }
  .headline text {
    font-family: "Anton", "Arial Narrow", sans-serif;
    fill: var(--ink);
    stroke: var(--outline);
    stroke-width: 3px;
    paint-order: stroke;
  }
  .release {
    position: absolute; left: 44px; top: 394px;
  }
  .release-tag {
    position: absolute; left: 14px; top: 0;
    background: var(--bench-red);
    color: var(--chip-white);
    font-family: "Archivo", sans-serif;
    font-weight: 800;
    font-size: 22px;
    letter-spacing: -0.5px;
    padding: 3px 10px;
    white-space: nowrap;
  }
  .release-title {
    position: absolute; left: 0; top: 34px;
    width: 330px; height: 106px;
    background: var(--ink);
    transform: rotate(-2deg);
    display: flex; align-items: center; justify-content: center;
  }
  .release-title span {
    font-family: "Rubik Dirt", "Impact", sans-serif;
    color: var(--cream);
    font-size: 50px;
    line-height: 1;
    white-space: nowrap;
  }
  .release-date {
    position: absolute; left: 8px; top: 144px;
    color: var(--ink);
    font-size: 26px;
    white-space: nowrap;
    transform: rotate(-4deg);
    transform-origin: left center;
  }
  .band-name {
    position: absolute; left: 708px; top: 431px;
    width: 378px; height: 65px;
    background: linear-gradient(90deg, var(--bench-green) 0%, var(--bench-yellow) 30%, var(--bench-orange) 55%, var(--bench-yellow) 75%, var(--bench-green) 100%);
    display: flex; align-items: center; justify-content: center;
    color: var(--ink);
    font-size: 31px;
    white-space: nowrap;
  }
  .featuring {
    position: absolute; left: 490px; top: 505px;
    width: 700px;
    display: flex; flex-direction: column; align-items: center;
  }
  .featuring-row { display: flex; justify-content: center; }
  .chip {
    font-size: 26px;
    line-height: 30px;
    padding: 0 5px;
    white-space: nowrap;
    text-transform: uppercase;
  }
  .chip--red { background: var(--bench-red); color: var(--chip-white); }
  .chip--red-yellow { background: var(--bench-red); color: var(--bench-yellow); }
  .chip--white-blue { background: var(--chip-white); color: var(--bench-blue); }
  .chip--white-red { background: var(--chip-white); color: var(--bench-red); }
  .chip--white-green { background: var(--chip-white); color: var(--bench-green); }
  .chip--dark { background: var(--chip-dark); color: var(--chip-white); }
  .chip--dark-red { background: var(--chip-dark); color: var(--bench-red); }
  .chip--dark-lime { background: var(--chip-dark); color: var(--bench-lime); }
</style>
</head>
<body>
<main class="cover">
  <div class="cover-photo" role="img" aria-label="Photograph of the artist relaxing on a rainbow-painted wooden bench beside an electric guitar, on a gravel road through green summer woods, with soft yellow, red and green colour smoke at the corners"></div>

  <svg class="headline" viewBox="0 0 966 392" aria-label="Brent Colfax">
    <text x="0" y="386" font-size="470" textLength="966" lengthAdjust="spacingAndGlyphs">BRENT COLFAX</text>
  </svg>

  <section class="release">
    <div class="release-tag">NEW SINGLE!</div>
    <div class="release-title"><span>WILLOW BEND</span></div>
    <div class="release-date">AVAILABLE EVERYWHERE 9/26</div>
  </section>

  <div class="band-name">AND THE KINSHIP CIRCLE</div>

  <section class="featuring">
    <div class="featuring-row">
      <span class="chip chip--red">Featuring:</span>
      <span class="chip chip--white-blue">Warren Petty,</span>
      <span class="chip chip--dark">Corey Halvin,</span>
      <span class="chip chip--white-red">Renata</span>
    </div>
    <div class="featuring-row">
      <span class="chip chip--white-red">Bloor,</span>
      <span class="chip chip--red-yellow">Ingrid Palumbo,</span>
      <span class="chip chip--dark-red">Martin "Chipper" Lowe,</span>
    </div>
    <div class="featuring-row">
      <span class="chip chip--dark-lime">Tamara Ridgely,</span>
      <span class="chip chip--white-blue">Wa Ni Po Glen Harker,</span>
    </div>
    <div class="featuring-row">
      <span class="chip chip--red-yellow">Nolan Brackett,</span>
      <span class="chip chip--white-green">Otis Crane,</span>
      <span class="chip chip--dark">Dustin Pell,</span>
    </div>
    <div class="featuring-row">
      <span class="chip chip--red">And The Final Grooveling</span>
    </div>
  </section>
</main>
</body>
</html>
```